Exercise Physiologist needs a Brochure

I am Exercise Physiologist providing exercise therapy for a variety of conditions. I have a logo and recent business card design. I like the black background like the front of the business cards. I have attached the flyer information required. I have also attached a few photos however they do not have to be used, happy to have no photos at all.

Industry/Entity Type

Health And Wellness

Font styles to use
Sans Serif

Requirements
Must have
• Please also add instagram @varnolhealth
Nice to have
• tri-fold brochure

```html
<!DOCTYPE html>
<html lang="en">
<head>
<meta charset="utf-8">
<title>Varnol Health &amp; Rehabilitation – Exercise Physiology</title>
<link href="https://fonts.googleapis.com/css2?family=Ubuntu:ital,wght@0,400;0,500;0,700;1,400;1,500&family=Kalam:wght@400;700&display=swap" rel="stylesheet">
<style>
  :root{
    --ink:#050608;
    --brand-blue:#0a71bd;
    --sky:#35b0e6;
    --heading-blue:#1d6cb6;
    --body-text:#454a50;
    --rule:#b9bcc0;
    --white:#ffffff;
  }
  *{margin:0;padding:0;box-sizing:border-box}
  html,body{width:934px;height:1200px;overflow:hidden;background:var(--white)}
  body{font-family:"Ubuntu",sans-serif;color:var(--body-text);position:relative}
  .brochure{position:relative;width:934px;height:1200px;overflow:hidden;
    background:linear-gradient(160deg,#ffffff 55%,#e9f1fa 100%)}
  .header-art{position:absolute;left:0;top:0;width:934px;height:470px}
  .practitioner{position:absolute;left:60px;top:64px;height:107px;border-left:5px solid var(--sky);padding-left:19px}
  .practitioner__name{font-weight:700;font-size:25px;color:var(--sky);line-height:1;margin-top:-2px}
  .practitioner__role{font-style:italic;font-weight:500;font-size:18.5px;color:var(--white);margin-top:6px}
  .practitioner__creds{list-style:none;font-style:italic;font-size:12px;color:var(--white);line-height:19px;margin-top:3px}
  .brand{position:absolute;left:578px;top:78px;display:flex;align-items:center;gap:12px}
  .brand__dot{width:78px;height:78px;border-radius:50%;background:var(--sky)}
  .brand__name{font-family:"Ubuntu",sans-serif;font-weight:400;font-size:54px;color:var(--sky);line-height:1}
  .headline{position:absolute;left:58px;top:194px;font-family:"Kalam",cursive;font-weight:400;font-size:38px;color:var(--sky);letter-spacing:.5px}
  .tagline{position:absolute;left:58px;top:248px;font-style:italic;font-weight:500;font-size:18.5px;line-height:30px;color:var(--white)}
  .section-title{font-family:"Kalam",cursive;font-weight:700;font-size:24px;color:var(--heading-blue);line-height:32px}
  .copy{font-size:14.6px;line-height:23.7px;color:var(--body-text)}
  .intro{position:absolute;left:54px;top:494px;width:800px}
  .intro .copy{margin-top:7px}
  .help{position:absolute;left:54px;top:628px;width:390px}
  .help .copy{margin-top:7px}
  .help .copy + .copy{margin-top:23.7px}
  .conditions{position:absolute;left:485px;top:628px;width:400px}
  .conditions ul{list-style:none;margin-top:8px}
  .conditions li{font-size:14.6px;line-height:25.2px;padding-left:21px;position:relative}
  .conditions li::before{content:"";position:absolute;left:2px;top:11px;width:4px;height:4px;border-radius:50%;background:var(--brand-blue)}
  .conditions .pullquote{font-family:"Kalam",cursive;font-size:15.5px;line-height:22.4px;color:var(--brand-blue);margin-top:16px}
  .divider{position:absolute;left:48px;top:1064px;width:839px;height:1px;background:var(--rule)}
  .contact{position:absolute;left:50px;top:1083px}
  .contact__call{font-family:"Kalam",cursive;font-size:15.5px;color:#333}
  .contact__phone{display:flex;align-items:center;gap:6px;font-weight:700;font-size:28px;color:var(--heading-blue);margin-top:2px}
  .contact__address{display:flex;align-items:center;gap:10px;font-size:13.3px;color:var(--brand-blue);margin-top:3px;padding-left:4px}
  .links{position:absolute;left:614px;top:1108px;list-style:none}
  .links li{display:flex;align-items:center;gap:12px;font-size:15.5px;color:var(--heading-blue);height:37px}
  .icon{flex:none}
</style>
</head>
<body>
<main class="brochure">
  <svg class="header-art" viewBox="0 0 934 470" aria-hidden="true">
    <path d="M0 318 Q470 452 934 256 V352 Q470 548 0 392 Z" fill="var(--brand-blue)"/>
    <path d="M0 0 H934 V256 Q470 467 0 312 Z" fill="var(--ink)"/>
  </svg>

  <header>
    <div class="practitioner">
      <h1 class="practitioner__name">Maren Ostby</h1>
      <p class="practitioner__role">Exercise Physiologist</p>
      <ul class="practitioner__creds">
        <li>B.AppSci – Human Mvmt</li>
        <li>Grad Dip – ExRehab</li>
        <li>Cert IV – Training &amp; Assessment</li>
      </ul>
    </div>
    <div class="brand">
      <span class="brand__dot"></span>
      <span class="brand__name">varnol</span>
    </div>
    <h2 class="headline">Heal through Movement</h2>
    <p class="tagline">Don’t let the right exercise but the wrong technique hinder your recovery<br>Discover how important the correct exercise technique is to your success</p>
  </header>

  <section class="intro">
    <h3 class="section-title">What is an Exercise Physiologist?</h3>
    <p class="copy">Exercise Physiologists are university educated health professionals trained to provide exercise therapy for pain and injury, pre and post surgery, mental health and chronic disease. They are registered providers with transport accident insurers, workplace insurers, public health schemes and veterans' services and many Private Health funds.</p>
  </section>

  <section class="help">
    <h3 class="section-title">How can I help you?</h3>
    <p class="copy">I have over 13 years of experience working as an Exercise Physiologist and have been working in the sport and fitness industry since 1996. I understand that everyone’s health and exercise experience is unique and will tailor a program to suit you and your lifestyle.</p>
    <p class="copy">Managing your condition involves working with you to develop the best exercises and teaching you the correct technique essential to improve. Home and gym based programs can be provided.</p>
    <p class="copy">When appropriate I can also work with your current treating health practitioner to provide a holistic approach to your recovery.</p>
  </section>

  <section class="conditions">
    <h3 class="section-title">Common conditions that<br>benefit from exercise therapy</h3>
    <ul>
      <li>Back pain</li>
      <li>Joint pain</li>
      <li>Pain relating to exercise</li>
      <li>Arthritis</li>
      <li>Anxiety relating to exercise</li>
      <li>Depression and Anxiety</li>
      <li>Chronic diseases such as diabetes, heart<br>and lung disease.</li>
      <li>Motor vehicle accidents</li>
    </ul>
    <p class="pullquote">Performing the right exercise the wrong way can do more harm than good. I can teach you what, how and when to perform your tailored exercise program to get the best results.</p>
  </section>

  <div class="divider"></div>

  <footer>
    <div class="contact">
      <p class="contact__call">Call or email me today to see how I can help you.</p>
      <p class="contact__phone">
        <svg class="icon" width="22" height="22" viewBox="0 0 24 24" aria-hidden="true"><path fill="var(--heading-blue)" d="M6.6 10.8a15.1 15.1 0 0 0 6.6 6.6l2.2-2.2a1 1 0 0 1 1-.25 11.4 11.4 0 0 0 3.6.57 1 1 0 0 1 1 1V20a1 1 0 0 1-1 1A17 17 0 0 1 3 4a1 1 0 0 1 1-1h3.5a1 1 0 0 1 1 1c0 1.25.2 2.45.57 3.6a1 1 0 0 1-.25 1z"/></svg>
        0400 555 019
      </p>
      <p class="contact__address">
        <svg class="icon" width="9" height="13" viewBox="0 0 10 14" aria-hidden="true"><path fill="var(--brand-blue)" d="M5 0a5 5 0 0 0-5 5c0 3.8 5 9 5 9s5-5.2 5-9a5 5 0 0 0-5-5zm0 7a2 2 0 1 1 0-4 2 2 0 0 1 0 4z"/></svg>
        Gate 4, 18 Harlow Quarry Rd EASTBROOK (Fenwick Fitness)
      </p>
    </div>
    <ul class="links">
      <li>
        <svg class="icon" width="20" height="14" viewBox="0 0 20 14" aria-hidden="true"><rect x="0.8" y="0.8" width="18.4" height="12.4" fill="none" stroke="var(--heading-blue)" stroke-width="1.6"/><path d="M1 1 L10 8 L19 1" fill="none" stroke="var(--heading-blue)" stroke-width="1.6"/></svg>
        hello@varnolhealth.com.au
      </li>
      <li>
        <svg class="icon" width="19" height="19" viewBox="0 0 19 19" aria-hidden="true"><rect width="19" height="19" rx="2" fill="var(--heading-blue)"/></svg>
        @varnolhealth
      </li>
    </ul>
  </footer>
</main>
</body>
</html>
```